Payment company requires web design

We need a web design for a new company based in Singapore.

The company focuses on providing 2 key products: 1) an alternative payment option (i.e. like zorbu or plendrixon options) on the traditional checkout process 2) a replacement/outsource of a merchants payment page. Key in the UX flow is a end customer dashboard that manages all payments.

We look to provide a simple, fluid and easy to use payment process. The dashboard is minimalistic that allows easy navigation, review of transactions and all available options through gamification.

The final design should communicate ease of use, flexibility and transparency.

The value is for the merchant - retail/travel/insurance companies. However its the merchant's end customers that are the target and who the UX is built for.

It Company

malvri

5+ page

ec1f27

• 7 pages mimicking UX flow
• payment page * 2 - 1) alternative payment type 2) outsource of merchants payment page to our business
• our landing page
• end customer verification page
• end customer registration
• customer dashboard
• UX flow in attached file
• open to ideas
• have asked for the logo to be added
• logo to have the colour red (chinese for prosperity)
• the company is all about flexibility, transparency in personal finance management with the option of instalment payments

```html
<!DOCTYPE html>
<html lang="en">
<head>
<meta charset="utf-8">
<title>malvri — Buy Now, Pay Later</title>
<link href="https://fonts.googleapis.com/css2?family=Open+Sans:ital,wght@0,400;0,600;0,700;1,400;1,600&family=Raleway:wght@300;400;600;700&display=swap" rel="stylesheet">
<style>
  :root {
    --navy-deep: #0b1550;
    --navy: #2b3f80;
    --navy-footer: #2e3563;
    --navy-bar: #262c55;
    --red: #ec1f27;
    --coral: #f05a5a;
    --coral-soft: #f7a29a;
    --white: #ffffff;
    --ink: #222;
    --grey: #666;
    --logo-grey: #8a8a8a;
  }
  * { margin: 0; padding: 0; box-sizing: border-box; }
  html, body { width: 673px; height: 1200px; overflow: hidden; }
  body { font-family: "Open Sans", Arial, sans-serif; color: var(--ink); background: var(--white); position: relative; }
  section, footer, header { position: absolute; left: 0; width: 673px; }
  .abs { position: absolute; }
  .center { text-align: center; left: 0; width: 673px; }

  /* Hero */
  .hero { top: 0; height: 265px; background: radial-gradient(ellipse at 50% 40%, #1c2d80 0%, #101c62 45%, var(--navy-deep) 100%); color: var(--white); }
  .brand { font-family: "Raleway", sans-serif; font-weight: 700; color: var(--white); display: flex; align-items: center; gap: 3px; }
  .brand-mark { width: 9px; height: 9px; background: var(--red); }
  .hero .brand { top: 8px; left: 0; width: 673px; justify-content: center; font-size: 21px; }
  .account-btn { top: 13px; height: 11px; border: 1px solid var(--white); border-radius: 6px; font-size: 5px; font-weight: 600; display: flex; align-items: center; justify-content: center; letter-spacing: .2px; }
  .account-btn.my { left: 454px; width: 39px; color: var(--white); }
  .account-btn.register { left: 501px; width: 30px; background: var(--white); color: var(--navy); }
  .hero-rule { top: 36px; left: 130px; width: 413px; height: 1px; background: rgba(255,255,255,.25); }
  .main-nav { top: 46px; left: 0; width: 673px; font-size: 5px; font-weight: 700; letter-spacing: .2px; }
  .main-nav span { position: absolute; white-space: nowrap; }
  .hero h1 { top: 110px; font-size: 24px; font-weight: 700; letter-spacing: .5px; }
  .hero p { top: 145px; font-size: 8.3px; line-height: 11.5px; }
  .btn { background: var(--red); color: var(--white); font-size: 5px; font-weight: 700; border-radius: 8px; display: flex; align-items: center; justify-content: center; }
  .hero .btn { top: 197px; left: 311px; width: 52px; height: 11px; }

  /* Features */
  .features { top: 265px; height: 153px; }
  .feature { position: absolute; top: 43px; width: 120px; margin-left: -60px; text-align: center; }
  .feature svg { display: block; margin: 0 auto; }
  .feature h3 { font-size: 5px; font-weight: 700; margin-top: 12px; letter-spacing: .2px; }
  .feature p { font-size: 4.3px; line-height: 7px; color: var(--grey); margin-top: 5px; }

  /* How it works */
  .how { top: 418px; height: 237px; background: linear-gradient(100deg, var(--coral-soft) 0%, var(--coral) 55%, #d94848 100%); color: var(--white); }
  .how h2 { top: 16px; font-size: 16px; font-weight: 700; }
  .how .lead { top: 52px; font-size: 8px; line-height: 10.5px; font-weight: 600; }
  .step-circle { top: 98px; width: 63px; height: 63px; margin-left: -31px; border-radius: 50%; background: #fde9e6; display: flex; align-items: center; justify-content: center; }
  .step-arrow { top: 126px; }
  .step-text { top: 169px; width: 112px; margin-left: -56px; text-align: center; font-size: 7.8px; line-height: 10px; font-weight: 600; }

  /* Buy on */
  .merchants { top: 655px; height: 145px; }
  .section-title { font-family: "Raleway", sans-serif; font-weight: 700; }
  .merchants h2 { top: 24px; font-size: 16px; color: var(--navy); }
  .merchant { position: absolute; top: 74px; transform: translateX(-50%); font-size: 11px; font-weight: 700; color: var(--logo-grey); white-space: nowrap; }
  .merchant.dark { color: #111; letter-spacing: 1px; font-size: 10px; }

  /* Testimonials */
  .testimonials { top: 800px; height: 177px; background: var(--navy); color: var(--white); }
  .testimonials h2 { top: 13px; font-size: 16px; color: #e9ecf6; }
  .portrait { top: 55px; left: 166px; width: 75px; height: 75px; border-radius: 50%; border: 2px solid #1d2b5c; background: linear-gradient(160deg, #a0583f 0%, #7b4a3a 60%, #c98070 100%); }
  .testimonial-body { top: 60px; left: 272px; width: 320px; display: flex; flex-direction: column; align-items: flex-start; }
  .quote { font-size: 12.4px; line-height: 15px; font-style: italic; letter-spacing: -.2px; }
  .quote-author { margin-top: 5px; font-size: 4.5px; font-weight: 700; letter-spacing: .2px; }
  .social { display: flex; gap: 3px; }
  .social span { width: 14px; height: 14px; border: 1px solid var(--white); }
  .testimonial-body .social { margin-top: 9px; }
  .dots { top: 160px; left: 311px; display: flex; gap: 5px; }
  .dots span { width: 6px; height: 6px; border-radius: 50%; background: #7b8bbd; }
  .dots span.active { background: var(--white); }

  /* CTA */
  .cta { top: 977px; height: 123px; }
  .cta h2 { top: 26px; font-family: "Raleway", sans-serif; font-weight: 400; font-size: 14px; color: #333; }
  .cta p { top: 44px; font-family: "Raleway", sans-serif; font-size: 10.5px; color: #444; }
  .cta .btn { top: 72px; left: 288px; width: 97px; height: 17px; }

  /* Footer */
  .site-footer { top: 1100px; height: 100px; background: var(--navy-footer); color: var(--white); }
  .footer-col { top: 24px; width: 120px; margin-left: -60px; text-align: center; }
  .footer-col h4 { font-size: 5px; font-weight: 700; letter-spacing: .2px; }
  .footer-col p { font-size: 4.3px; line-height: 7px; margin-top: 5px; color: #dde; }
  .site-footer .brand { top: 16px; left: 0; width: 673px; justify-content: center; font-size: 18px; }
  .footer-rule { top: 50px; left: 302px; width: 70px; height: 1px; background: rgba(255,255,255,.4); }
  .site-footer .social { top: 60px; left: 312px; }
  .copyright { top: 88px; height: 12px; background: var(--navy-bar); font-size: 4.3px; color: #aab; display: flex; align-items: center; justify-content: center; }
</style>
</head>
<body>

<header class="hero" role="img" aria-label="Deep blue night backdrop with soft bokeh lights and faint snowflakes">
  <div class="abs brand"><span class="brand-mark"></span>malvri</div>
  <div class="abs account-btn my">MY ACCOUNT</div>
  <div class="abs account-btn register">REGISTER</div>
  <div class="abs hero-rule"></div>
  <nav class="abs main-nav">
    <span style="left:244px">HOME</span>
    <span style="left:281px">SERVICES</span>
    <span style="left:319px">INFORMATION</span>
    <span style="left:364px">CUSTOMERS</span>
    <span style="left:415px">FAQ &#8964;</span>
  </nav>
  <h1 class="abs center">BUY NOW, PAY LATER</h1>
  <p class="abs center">Lorem ipsum dolor sit amet, consectetur adipiscing elit. Praesent commodo cursus magna<br>vel scelerisque nisl consectetur et.</p>
  <div class="abs btn">FIND OUT MORE</div>
</header>

<section class="features">
  <div class="feature" style="left:185px">
    <svg width="28" height="22" viewBox="0 0 28 22" fill="none" stroke="#ec1f27" stroke-width="1.2"><rect x="2" y="1" width="24" height="15"/><rect x="4" y="3" width="20" height="11"/><path d="M10 20h8M14 16v4"/></svg>
    <h3>EASY TO USE</h3>
    <p>Cras justo odio, dapibus ac facilisis in, egestas eget quam. Nullam quis risus eget urna mollis ornare vel eu leo. Donec ullamcorper nulla non metus auctor</p>
  </div>
  <div class="feature" style="left:337px">
    <svg width="28" height="22" viewBox="0 0 28 22" fill="none" stroke="#ec1f27" stroke-width="1.2"><path d="M14 1a7 7 0 0 0-4 12.7V16h8v-2.3A7 7 0 0 0 14 1z"/><path d="M11 18h6M12 20.5h4"/></svg>
    <h3>MODERN PAYMENTS</h3>
    <p>Cras justo odio, dapibus ac facilisis in, egestas eget quam. Nullam quis risus eget urna mollis ornare vel eu leo. Donec ullamcorper nulla non metus auctor</p>
  </div>
  <div class="feature" style="left:488px">
    <svg width="28" height="22" viewBox="0 0 28 22" fill="none" stroke="#ec1f27" stroke-width="1.2"><rect x="2" y="5" width="24" height="16"/><path d="M10 5V2h8v3M2 11h24M13 10h2v3h-2z"/></svg>
    <h3>KEEP SAVED</h3>
    <p>Cras justo odio, dapibus ac facilisis in, egestas eget quam. Nullam quis risus eget urna mollis ornare vel eu leo. Donec ullamcorper nulla non metus auctor</p>
  </div>
</section>

<section class="how" role="img" aria-label="Coral-tinted backdrop of hands paying by card at a laptop with faint finance symbols">
  <h2 class="abs center">HOW IT WORKS?</h2>
  <p class="abs center lead">Lorem ipsum dolor sit amet, consectetur adipiscing elit. Vestibulum molestie augue dui, non tincidunt<br>neque fermentum in. Vivamus ultrices aliquam lacinia. Nullam et nunc in lacus consectetur posuere.</p>

  <div class="abs step-circle" style="left:219px">
    <svg width="22" height="24" viewBox="0 0 22 24" fill="#c8161e"><circle cx="11" cy="7" r="6"/><path d="M1 24c0-7 4-10 10-10s10 3 10 10z"/></svg>
  </div>
  <svg class="abs step-arrow" style="left:270px" width="18" height="6" viewBox="0 0 18 6" fill="#fde9e6"><path d="M0 2h13V0l5 3-5 3V4H0z"/></svg>
  <div class="abs step-circle" style="left:337px">
    <svg width="32" height="22" viewBox="0 0 32 22"><rect width="32" height="22" rx="2" fill="#c8161e"/><rect y="5" width="32" height="4" fill="#fde9e6"/><rect x="4" y="14" width="8" height="2" fill="#fde9e6"/><rect x="14" y="14" width="5" height="2" fill="#fde9e6"/></svg>
  </div>
  <svg class="abs step-arrow" style="left:389px" width="18" height="6" viewBox="0 0 18 6" fill="#fde9e6"><path d="M0 2h13V0l5 3-5 3V4H0z"/></svg>
  <div class="abs step-circle" style="left:454px">
    <svg width="28" height="24" viewBox="0 0 28 24" fill="#c8161e"><path d="M0 1h5l1 3h22l-3 11H9L5 3H0z"/><rect x="9" y="16" width="15" height="2"/><circle cx="11" cy="21" r="2.5"/><circle cx="22" cy="21" r="2.5"/></svg>
  </div>

  <p class="abs step-text" style="left:219px">Lorem ipsum dolor sit amet, consectetur adipiscing elit. Vestibulum molestie .</p>
  <p class="abs step-text" style="left:337px">Lorem ipsum dolor sit amet, consectetur adipiscing elit. Vestibulum molestie .</p>
  <p class="abs step-text" style="left:454px">Lorem ipsum dolor sit amet, consectetur adipiscing elit. Vestibulum molestie .</p>
</section>

<section class="merchants">
  <h2 class="abs center section-title">BUY ON</h2>
  <span class="merchant dark" style="left:117px">NORVELLE</span>
  <span class="merchant" style="left:204px">Talkora</span>
  <span class="merchant" style="left:291px; font-size:8px; color:#333">Mirelo Store</span>
  <span class="merchant" style="left:380px; font-size:13px">pindle</span>
  <span class="merchant" style="left:469px">staynest</span>
  <span class="merchant" style="left:557px; font-size:13px; color:#666">bidzo</span>
</section>

<section class="testimonials">
  <h2 class="abs center section-title">TESTIMONIALS</h2>
  <div class="abs portrait" role="img" aria-label="Portrait of a smiling customer against a brick wall"></div>
  <div class="abs testimonial-body">
    <p class="quote">“Integer posuere erat a ante venenatis dapibus posuere<br>velit aliquet. Donec sed odio dui. Aenean eu leo quam...”</p>
    <p class="quote-author">DANA RELL, TERVAN DESIGNER AT XXX</p>
    <div class="social"><span></span><span></span><span></span></div>
  </div>
  <div class="abs dots"><span></span><span class="active"></span><span></span><span></span><span></span></div>
</section>

<section class="cta">
  <h2 class="abs center">Are You Ready to Start?</h2>
  <p class="abs center">Click on the button below to become a member</p>
  <div class="abs btn">JOIN TODAY!</div>
</section>

<footer class="site-footer">
  <div class="abs footer-col" style="left:198px">
    <h4>LOCATION</h4>
    <p>88 Orchard Row<br>Westvale, WV 10101</p>
  </div>
  <div class="abs brand"><span class="brand-mark"></span>malvri</div>
  <div class="abs footer-rule"></div>
  <div class="abs social"><span></span><span></span><span></span></div>
  <div class="abs footer-col" style="left:473px">
    <h4>ABOUT MALVRI</h4>
    <p>Cras justo odio, dapibus ac facilisis in, egestas eget quam. Donec ullamcorper nulla non metus auctor fringilla.</p>
  </div>
  <div class="abs center copyright">Copyright © 2016. All Rights Reserved</div>
</footer>

</body>
</html>
```